IT CEO and Real Estate Investor

It should include two roles and be a two sided card (both roles can be one a single side with a creative view or on different sides).
Card must be creative and interesting, but still professional.
Phone countries(USA/Russia) might be as flags or words, whatever works better.
Boris Melnovetz
Skype: boris_m
E-mail: melnovetz@quorbamail.com
Facebook: plavbook.example/melnovetz
Linkedin: trelnet.example/in/melnovetz
Phone (US): 1(555)316-2947
Phone (RUS): 7(955)482-3170
First role:
Pex Lattor (pexlattor.example) - include logo or part of logo (the $)
E-Commerce Automation Solutions
Founder/CEO/CTO
Second role:
Real Estate Investor
Dunmere, OH
UPDATE:
Let's do one side as logo only and all information on the other side - I don't like designs with information on both sides.
I also really liked designs on black (or other dark) background

```html
<!DOCTYPE html>
<html lang="en">
<head>
<meta charset="utf-8">
<title>Pex Lattor business cards</title>
<link rel="stylesheet" href="https://fonts.googleapis.com/css2?family=Lato:wght@400;700&display=swap">
<style>
  :root {
    --brand-blue: #29a9e1;
    --ink: #222222;
    --card-white: #ffffff;
    --card-dark: #333333;
    --band-dark: #3a3a3a;
    --stage-top: #1c1c1c;
    --stage-bottom: #0b0b0b;
    --flag-red: #d52b1e;
    --flag-blue: #1c3f94;
    --flag-navy: #3c3b6e;
  }
  * { box-sizing: border-box; margin: 0; padding: 0; }
  html, body { width: 1200px; height: 741px; overflow: hidden; }
  body {
    font-family: "Lato", sans-serif;
    background: radial-gradient(ellipse at 50% 45%, var(--stage-top), var(--stage-bottom) 80%);
    position: relative;
  }
  .card {
    position: absolute;
    width: 494px;
    height: 281px;
    border-radius: 13px;
    overflow: hidden;
    box-shadow: 0 4px 12px rgba(0,0,0,0.7);
  }
  .card--front { top: 74px; background: var(--card-white); color: var(--ink); }
  .card--back { top: 383px; display: flex; align-items: center; justify-content: center; }
  .card--left { left: 82px; }
  .card--right { left: 595px; }
  .card--back-blue { background: var(--brand-blue); }
  .card--back-dark { background: var(--card-dark); }

  .brand { position: absolute; left: 23px; top: 37px; display: flex; align-items: center; gap: 24px; }
  .brand__mark { width: 72px; height: 72px; background: var(--brand-blue); flex: none; }
  .brand__name {
    font-weight: 700; font-size: 42px; letter-spacing: 5px;
    color: var(--brand-blue); text-transform: uppercase; white-space: nowrap;
  }
  .card--back .brand { position: static; gap: 24px; }
  .card--back .brand__mark { background: var(--card-white); width: 80px; height: 80px; }
  .card--back .brand__name { color: var(--card-white); font-size: 44px; }

  .identity { position: absolute; right: 22px; top: 138px; text-align: right; }
  .identity__name { font-weight: 700; font-size: 18.5px; color: var(--brand-blue); text-transform: uppercase; line-height: 1.1; }
  .identity__role { font-size: 13.5px; line-height: 1.08; }

  .divider { position: absolute; left: 23px; top: 178px; width: 323px; height: 1.5px; background: var(--brand-blue); }

  .contacts { position: absolute; left: 23px; top: 184px; list-style: none; }
  .contacts li { display: flex; align-items: center; gap: 5px; font-size: 14.5px; height: 17.7px; }
  .contacts__icon { width: 14px; height: 14px; background: var(--brand-blue); border-radius: 2px; flex: none; }

  .phones { position: absolute; right: 22px; top: 216px; list-style: none; }
  .phones li { display: flex; align-items: center; justify-content: flex-end; gap: 10px; font-size: 14.5px; height: 17.5px; }
  .flag { width: 20px; height: 11px; flex: none; display: block; }

  .footer-band { position: absolute; left: 0; bottom: 0; width: 494px; height: 24px; }
</style>
</head>
<body>

  <section class="card card--front card--left">
    <div class="brand"><span class="brand__mark"></span><span class="brand__name">Pex Lattor</span></div>
    <div class="identity">
      <p class="identity__name">Boris Melnovetz</p>
      <p class="identity__role">E-Commerce Automation Solutions</p>
      <p class="identity__role">Founder/CEO/CTO</p>
    </div>
    <div class="divider"></div>
    <ul class="contacts">
      <li><span class="contacts__icon"></span>boris_m</li>
      <li><span class="contacts__icon"></span>melnovetz@quorbamail.com</li>
      <li><span class="contacts__icon"></span>plavbook.example/melnovetz</li>
      <li><span class="contacts__icon"></span>trelnet.example/in/melnovetz</li>
    </ul>
    <ul class="phones">
      <li>
        <svg class="flag" viewBox="0 0 20 11" aria-label="USA"><rect width="20" height="11" fill="#fff"/><g fill="var(--flag-red)"><rect y="0" width="20" height="1.6"/><rect y="3.2" width="20" height="1.6"/><rect y="6.4" width="20" height="1.6"/><rect y="9.4" width="20" height="1.6"/></g><rect width="8" height="6" fill="var(--flag-navy)"/></svg>
        1(555)316-2947
      </li>
      <li>
        <svg class="flag" viewBox="0 0 20 11" aria-label="Russia"><rect width="20" height="3.7" fill="#fff"/><rect y="3.7" width="20" height="3.6" fill="var(--flag-blue)"/><rect y="7.3" width="20" height="3.7" fill="var(--flag-red)"/></svg>
        7(955)482-3170
      </li>
    </ul>
    <svg class="footer-band" viewBox="0 0 494 24" preserveAspectRatio="none"><rect y="9" width="494" height="15" fill="var(--band-dark)"/><polygon points="280,0 494,0 494,24 272,24" fill="var(--brand-blue)"/></svg>
  </section>

  <section class="card card--front card--right">
    <div class="brand"><span class="brand__mark"></span><span class="brand__name">Pex Lattor</span></div>
    <div class="identity">
      <p class="identity__name">Boris Melnovetz</p>
      <p class="identity__role">Real Estate Investor</p>
      <p class="identity__role">Dunmere, OH</p>
    </div>
    <div class="divider"></div>
    <ul class="contacts">
      <li><span class="contacts__icon"></span>boris_m</li>
      <li><span class="contacts__icon"></span>melnovetz@quorbamail.com</li>
      <li><span class="contacts__icon"></span>plavbook.example/melnovetz</li>
      <li><span class="contacts__icon"></span>trelnet.example/in/melnovetz</li>
    </ul>
    <ul class="phones">
      <li>
        <svg class="flag" viewBox="0 0 20 11" aria-label="USA"><rect width="20" height="11" fill="#fff"/><g fill="var(--flag-red)"><rect y="0" width="20" height="1.6"/><rect y="3.2" width="20" height="1.6"/><rect y="6.4" width="20" height="1.6"/><rect y="9.4" width="20" height="1.6"/></g><rect width="8" height="6" fill="var(--flag-navy)"/></svg>
        1(555)316-2947
      </li>
      <li>
        <svg class="flag" viewBox="0 0 20 11" aria-label="Russia"><rect width="20" height="3.7" fill="#fff"/><rect y="3.7" width="20" height="3.6" fill="var(--flag-blue)"/><rect y="7.3" width="20" height="3.7" fill="var(--flag-red)"/></svg>
        7(955)482-3170
      </li>
    </ul>
    <svg class="footer-band" viewBox="0 0 494 24" preserveAspectRatio="none"><rect y="9" width="494" height="15" fill="var(--band-dark)"/><polygon points="280,0 494,0 494,24 272,24" fill="var(--brand-blue)"/></svg>
  </section>

  <section class="card card--back card--back-blue card--left">
    <div class="brand"><span class="brand__mark"></span><span class="brand__name">Pex Lattor</span></div>
  </section>

  <section class="card card--back card--back-dark card--right">
    <div class="brand"><span class="brand__mark"></span><span class="brand__name">Pex Lattor</span></div>
  </section>

</body>
</html>
```